Interior Design/ New Construction interior finishes

Interior Design Website

Target Market(s)

Home builders, New Construction, Renovations, Public

Industry/Entity Type

Construction

Coding

Coded - Design and coding required

Number of Pages Required

1 page

Font styles to use
Sans Serif

Colors

Designer to choose colors to be used in the design.

Requirements
Must have
• Section to upload pictures of projects
• Simple and modern design
• Designer 1 details about myself
• Logo
• Upload section for photos for future jobs
Nice to have
• Sections they can click on to see certain rooms in a house
• Decorating, floral arrangements, holiday decorating.
• I have lots of before and after as well. Maybe a section for those.

```html
<!DOCTYPE html>
<html lang="en">
<head>
<meta charset="utf-8">
<title>Nova Designs — Interior Design</title>
<link rel="stylesheet" href="https://fonts.googleapis.com/css2?family=Bebas+Neue&family=Open+Sans:ital,wght@0,400;0,600;0,700;1,400&display=swap">
<style>
:root{
  --orange:#d35a2b;
  --ink:#222222;
  --text:#555555;
  --muted:#8a8a8a;
  --light:#f1f1f1;
  --white:#ffffff;
  --wood:#7a4a32;
}
*{box-sizing:border-box;margin:0;padding:0}
html,body{width:1200px;height:5114px;overflow:hidden}
body{position:relative;background:var(--white);font-family:"Open Sans",Arial,sans-serif;color:var(--text)}
.section{position:absolute;left:0;width:1200px;overflow:hidden}
.abs{position:absolute}
.photo{position:absolute;display:block}
.section-title{position:absolute;left:160px;font-family:"Bebas Neue",Impact,sans-serif;font-size:64px;line-height:66px;color:var(--ink);font-weight:400}
.section-title .accent{color:var(--orange)}
.copy{font-size:11px;line-height:16px;color:var(--text)}
.btn{position:absolute;display:block;font-family:"Open Sans",Arial,sans-serif;font-weight:700;font-size:10px;letter-spacing:.5px;color:var(--white);text-align:center;text-transform:uppercase;text-decoration:none}
.btn--solid{background:var(--orange)}
.btn--ghost{border:2px solid var(--white)}

/* hero */
.hero{top:0;height:648px;background:linear-gradient(180deg,#8a4a30 0%,#a9573a 45%,#6b3a28 100%)}
.brand{position:absolute;left:104px;top:28px;display:flex;align-items:center;gap:12px;color:var(--white);font-size:30px;font-weight:400;letter-spacing:2px}
.brand-mark{width:50px;height:50px;border:2px solid var(--white);border-radius:50%}
.main-nav{position:absolute;left:540px;top:56px;display:flex;gap:22px}
.main-nav a{font-family:"Bebas Neue",Impact,sans-serif;font-size:16px;color:var(--white);text-decoration:none;letter-spacing:.5px}
.main-nav a.active{border-bottom:2px solid var(--white)}
.social-stack{position:absolute;left:1062px;top:34px;display:flex;flex-direction:column;gap:22px}
.social-stack span{display:block;width:46px;height:46px;background:rgba(255,255,255,.85)}
.hero-title{position:absolute;left:160px;top:290px;font-family:"Bebas Neue",Impact,sans-serif;font-size:62px;line-height:58px;color:var(--white);letter-spacing:1px;font-weight:400}
.hero-title .accent{color:var(--orange)}
.hero-lead{position:absolute;left:160px;top:410px;width:640px;font-style:italic;font-size:17px;line-height:21px;color:var(--white)}

/* about */
.about{top:648px;height:597px}
.about-copy{position:absolute;left:160px;top:276px;width:240px}
.features{position:absolute;left:420px;top:17px;width:323px;height:570px;background:linear-gradient(180deg,#b9613b 0%,#8b4a2f 40%,#5c3a28 70%,#7a5d45 100%)}
.feature-label{position:absolute;right:530px;text-align:right;font-family:"Bebas Neue",Impact,sans-serif;color:var(--white);font-size:22px;line-height:22px}
.feature-label small{display:block;font-size:13px;line-height:14px;color:#f3c4ae}
.feature-text{position:absolute;left:760px;width:380px}

/* services */
.services{top:1245px;height:596px;background:var(--light)}

/* blog */
.blog{top:1841px;height:580px}
.post-title{font-family:"Bebas Neue",Impact,sans-serif;font-size:17px;font-weight:400;color:var(--ink);margin-bottom:4px}
.date-badge{position:absolute;width:44px;height:44px;background:var(--orange);color:var(--white);font-family:"Bebas Neue",Impact,sans-serif;font-size:28px;line-height:44px;text-align:center}

/* team */
.team{top:2421px;height:494px;background:var(--light)}
.team-wire{position:absolute;top:0;width:1px;background:#9a9a9a}

/* portfolio */
.portfolio{top:2915px;height:699px}

/* packages */
.packages{top:3614px;height:597px;background:var(--light)}
.plan{position:absolute;top:52px;width:194px;height:511px;background:var(--white);text-align:center}
.plan svg{margin-top:40px}
.plan-name{margin-top:20px;font-family:"Bebas Neue",Impact,sans-serif;font-size:26px;line-height:26px;color:var(--ink)}
.plan-role{font-family:"Bebas Neue",Impact,sans-serif;font-size:13px;color:var(--orange)}
.plan-copy{margin:16px auto 0;width:150px;font-size:10px;line-height:14px;color:var(--muted)}
.plan-price{margin-top:22px;font-family:"Bebas Neue",Impact,sans-serif;font-size:46px;color:var(--ink)}
.plan .btn{left:50%;transform:translateX(-50%);bottom:44px;width:80px;height:26px;line-height:26px}

/* contact */
.contact{top:4211px;height:597px}
.contact-item{position:absolute;left:160px;display:flex;gap:18px}
.contact-item h4{font-family:"Bebas Neue",Impact,sans-serif;font-size:17px;font-weight:400;color:var(--orange);line-height:18px}
.contact-item p{font-size:10px;line-height:14px;color:var(--text);width:230px}
.social-row{position:absolute;left:160px;top:560px;display:flex;gap:10px}
.social-row span{display:block;width:26px;height:26px;background:var(--ink)}

/* map & footer */
.map{top:4808px;height:239px}
.site-footer{top:5047px;height:67px;text-align:center;font-size:10px;line-height:67px;color:var(--muted)}
</style>
</head>
<body>

<!-- HERO -->
<header class="section hero">
  <div class="photo" role="img" aria-label="Living room with patchwork sofa against a terracotta wall with framed art" style="inset:0;background:linear-gradient(180deg,#9b5035 0%,#b5623f 40%,#7d4a36 70%,#5a3a2c 100%)"></div>
  <div class="photo" style="inset:0;background:rgba(0,0,0,.18)"></div>
  <div class="brand"><span class="brand-mark"></span>Nova Designs</div>
  <nav class="main-nav">
    <a class="active" href="#">Home</a><a href="#">About Us</a><a href="#">Services</a><a href="#">Portfolio</a><a href="#">Our Team</a><a href="#">News</a><a href="#">Contact</a>
  </nav>
  <div class="social-stack" aria-label="Social links"><span></span><span></span><span></span></div>
  <h1 class="hero-title">Welcome to the <span class="accent">Nova</span><br><span class="accent">Designs</span> Agency</h1>
  <p class="hero-lead">Lorem ipsum dolor sit amet, consectetur adipiscing elit, sed do eiusmod tempor incididunt ut labore et dolore magna aliqua. Ut</p>
  <a class="btn btn--solid" href="#" style="left:160px;top:470px;width:120px;height:38px;line-height:38px">Read More</a>
  <a class="btn btn--ghost" href="#" style="left:318px;top:470px;width:130px;height:38px;line-height:34px">Read More</a>
</header>

<!-- ABOUT -->
<section class="section about">
  <h2 class="section-title" style="top:72px">About<br><span class="accent">Nova</span><br>Designs</h2>
  <p class="copy about-copy">Lorem ipsum dolor sit amet, consectetur adipiscing elit, sed do eiusmod tempor incididunt ut labore et dolore magna aliqua. Ut enim ad minim veniam, quis nostrud exercitation ullamco laboris nisi ut aliquip ex ea commodo consequat. Lorem ipsum dolor sit amet, consectetur adipiscing elit, sed do eiusmod tempor incididunt ut labore et dolore magna aliqua. Ut enim ad minim veniam, quis nostrud exercitation ullamco laboris nisi ut aliquip ex ea commodo consequat.</p>
  <div class="features" role="img" aria-label="Tall photo of a house exterior and decorated rooms under an orange tint"></div>
  <div class="feature-label" style="top:68px">Working Hours<small>Rooms</small></div>
  <div class="feature-label" style="top:187px">Working Hours<small>Decorating</small></div>
  <div class="feature-label" style="top:317px">Working Hours<small>Floral Arrangements</small></div>
  <div class="feature-label" style="top:450px">Working Hours<small>Holiday Decorating</small></div>
  <svg class="abs" style="left:682px;top:57px" width="54" height="460" viewBox="0 0 54 460" aria-hidden="true">
    <g fill="#fff" stroke="#d35a2b" stroke-width="3">
      <circle cx="27" cy="27" r="24"/><circle cx="27" cy="146" r="24"/><circle cx="27" cy="276" r="24"/><circle cx="27" cy="409" r="24"/>
    </g>
    <g fill="none" stroke="#d35a2b" stroke-width="2" stroke-linecap="round">
      <path d="M19 35 L33 21 M30 18 L36 24"/><path d="M19 154 L33 140 M30 137 L36 143"/>
      <path d="M19 284 L33 270 M30 267 L36 273"/><path d="M19 417 L33 403 M30 400 L36 406"/>
    </g>
  </svg>
  <p class="copy feature-text" style="top:51px">Lorem ipsum dolor sit amet, consectetur adipiscing elit, sed do eiusmod tempor incididunt ut labore et dolore magna aliqua. Ut enim ad minim veniam, quis nostrud exercitation ullamco</p>
  <p class="copy feature-text" style="top:170px">Lorem ipsum dolor sit amet, consectetur adipiscing elit, sed do eiusmod tempor incididunt ut labore et dolore magna aliqua. Ut enim ad minim veniam, quis nostrud exercitation ullamco</p>
  <p class="copy feature-text" style="top:300px">Lorem ipsum dolor sit amet, consectetur adipiscing elit, sed do eiusmod tempor incididunt ut labore et dolore magna aliqua. Ut enim ad minim veniam, quis nostrud exercitation ullamco</p>
  <p class="copy feature-text" style="top:429px">Lorem ipsum dolor sit amet, consectetur adipiscing elit, sed do eiusmod tempor incididunt ut labore et dolore magna aliqua. Ut enim ad minim veniam, quis nostrud exercitation ullamco</p>
</section>

<!-- SERVICES -->
<section class="section services">
  <div class="photo" role="img" aria-label="Bright kitchen with island" style="left:420px;top:58px;width:190px;height:225px;background:linear-gradient(160deg,#c9c3b8,#8d7f70)"></div>
  <div class="photo" role="img" aria-label="Dining room with chandelier" style="left:632px;top:58px;width:194px;height:225px;background:linear-gradient(160deg,#c7a98a,#6e5442)"></div>
  <div class="photo" role="img" aria-label="Living room with large windows" style="left:846px;top:58px;width:194px;height:225px;background:linear-gradient(160deg,#b3ae9f,#6f6a5a)"></div>
  <div class="photo" role="img" aria-label="White bathroom with vanity" style="left:420px;top:307px;width:190px;height:221px;background:linear-gradient(160deg,#d8d6d2,#9c958b)"></div>
  <div class="photo" role="img" aria-label="Open living area with neutral tones" style="left:632px;top:307px;width:194px;height:221px;background:linear-gradient(160deg,#d2cdc4,#8f8577)"></div>
  <div class="photo" role="img" aria-label="Bedroom with soft lighting" style="left:846px;top:307px;width:194px;height:221px;background:linear-gradient(160deg,#cfc3b0,#8a7862)"></div>
  <h2 class="section-title" style="top:358px">Our<br><span class="accent">Special</span><br>Services</h2>
</section>

<!-- BLOG -->
<section class="section blog">
  <div class="photo" role="img" aria-label="Kitchen with dark cabinets" style="left:420px;top:62px;width:194px;height:133px;background:linear-gradient(160deg,#a89886,#4f4338)"></div>
  <div class="date-badge" style="left:420px;top:138px">24</div>
  <div class="abs" style="left:634px;top:60px;width:190px"><h3 class="post-title">Designed and built with care</h3><p class="copy">Lorem ipsum dolor sit amet, consectetur adipiscing elit, sed do eiusmod tempor incididunt ut labore et dolore magna aliqua. Ut enim ad minim</p></div>

  <div class="photo" role="img" aria-label="White living room with sofa" style="left:420px;top:215px;width:194px;height:133px;background:linear-gradient(160deg,#dcdad6,#8f8a82)"></div>
  <div class="date-badge" style="left:420px;top:291px">24</div>
  <div class="abs" style="left:634px;top:213px;width:190px"><h3 class="post-title">Designed and built with care</h3><p class="copy">Lorem ipsum dolor sit amet, consectetur adipiscing elit, sed do eiusmod tempor incididunt ut labore et dolore magna aliqua. Ut enim ad minim</p></div>

  <div class="photo" role="img" aria-label="Bedroom with warm wood tones" style="left:420px;top:375px;width:194px;height:137px;background:linear-gradient(160deg,#b58f6b,#5b4231)"></div>
  <div class="date-badge" style="left:420px;top:455px">24</div>
  <div class="abs" style="left:634px;top:373px;width:190px"><h3 class="post-title">Designed and built with care</h3><p class="copy">Lorem ipsum dolor sit amet, consectetur adipiscing elit, sed do eiusmod tempor incididunt ut labore et dolore magna aliqua. Ut enim ad minim</p></div>

  <div class="photo" role="img" aria-label="Tall photo of a carved wood mantel mirror above a fireplace" style="left:843px;top:62px;width:197px;height:450px;background:linear-gradient(180deg,#e2ddd5,#a99a86 55%,#5e5247)"></div>
  <div class="date-badge" style="left:843px;top:62px">24</div>
  <h2 class="section-title" style="top:342px">Latest<br><span class="accent">Design</span><br>Blog</h2>
</section>

<!-- TEAM -->
<section class="section team">
  <div class="team-wire" style="left:552px;height:123px"></div>
  <div class="team-wire" style="left:794px;height:123px"></div>
  <div class="team-wire" style="left:1033px;height:123px"></div>
  <div class="photo" role="img" aria-label="Team member portfolio photo of a dining room" style="left:447px;top:123px;width:211px;height:259px;background:linear-gradient(160deg,#d8d4cd,#7b7266);box-shadow:0 8px 14px rgba(0,0,0,.25)"></div>
  <div class="photo" role="img" aria-label="Team member portfolio photo of a kitchen" style="left:689px;top:123px;width:211px;height:259px;background:linear-gradient(160deg,#e0ddd8,#8d8578);box-shadow:0 8px 14px rgba(0,0,0,.25)"></div>
  <div class="photo" role="img" aria-label="Team member portfolio photo of a mantel" style="left:928px;top:123px;width:211px;height:259px;background:linear-gradient(160deg,#e4e1dc,#9b8f7f);box-shadow:0 8px 14px rgba(0,0,0,.25)"></div>
  <h2 class="section-title" style="top:249px">Creative<br><span class="accent">Team</span><br>Members</h2>
</section>

<!-- PORTFOLIO -->
<section class="section portfolio">
  <div class="photo" role="img" aria-label="Great room with wooden beams" style="left:0;top:0;width:307px;height:307px;background:linear-gradient(160deg,#8c6a4f,#3f3127)"></div>
  <div class="photo" role="img" aria-label="Wine cellar behind glass" style="left:307px;top:0;width:290px;height:307px;background:linear-gradient(160deg,#9a8470,#4a3c31)"></div>
  <div class="photo" role="img" aria-label="White kitchen with pendant lights" style="left:597px;top:0;width:307px;height:307px;background:linear-gradient(160deg,#e5e3df,#a59e95)"></div>
  <div class="photo" role="img" aria-label="Sunroom with dark window frames" style="left:904px;top:0;width:296px;height:307px;background:linear-gradient(160deg,#d9d6d0,#6d665d)"></div>
  <div class="photo" role="img" aria-label="White built-in cabinetry" style="left:0;top:307px;width:240px;height:392px;background:linear-gradient(160deg,#efeeeb,#b8b3ab)"></div>
  <h2 class="section-title" style="left:280px;top:455px">Our<br><span class="accent">Portfolio</span><br>Gallery</h2>
  <div class="photo" role="img" aria-label="Kitchen with dark grey cabinets and wall lights" style="left:597px;top:307px;width:603px;height:392px;background:linear-gradient(160deg,#c2bbb1,#6a635b 60%,#4b4640)"></div>
</section>

<!-- PACKAGES -->
<section class="section packages">
  <div class="plan" style="left:420px">
    <svg width="40" height="44" viewBox="0 0 40 44" fill="none" stroke="#222" stroke-width="2" aria-hidden="true"><path d="M20 3a13 13 0 0 0-8 23v6h16v-6a13 13 0 0 0-8-23z"/><path d="M14 36h12M16 41h8"/></svg>
    <div class="plan-name">Designer Name</div><div class="plan-role">Graphic Designer</div>
    <p class="plan-copy">Lorem ipsum dolor sit amet, consectetur adipiscing elit, sed do eiusmod tempor incididunt ut labore et dolore magna aliqua. Ut enim ad minim veniam, quis nostrud exercitation.</p>
    <div class="plan-price">$500</div>
    <a class="btn btn--solid" href="#">Read More</a>
  </div>
  <div class="plan" style="left:634px">
    <svg width="46" height="44" viewBox="0 0 46 44" fill="none" stroke="#222" stroke-width="2" aria-hidden="true"><path d="M2 4h7l6 26h24l5-18H12"/><circle cx="18" cy="38" r="3"/><circle cx="36" cy="38" r="3"/></svg>
    <div class="plan-name">Designer Name</div><div class="plan-role">Graphic Designer</div>
    <p class="plan-copy">Lorem ipsum dolor sit amet, consectetur adipiscing elit, sed do eiusmod tempor incididunt ut labore et dolore magna aliqua. Ut enim ad minim veniam, quis nostrud exercitation.</p>
    <div class="plan-price">$5000</div>
    <a class="btn btn--solid" href="#">Read More</a>
  </div>
  <div class="plan" style="left:846px">
    <svg width="44" height="44" viewBox="0 0 44 44" fill="none" stroke="#222" stroke-width="2" aria-hidden="true"><rect x="8" y="3" width="33" height="30"/><rect x="3" y="10" width="33" height="31" fill="#fff"/><circle cx="13" cy="19" r="3"/><path d="M5 37l10-10 7 6 6-5 8 7"/></svg>
    <div class="plan-name">Designer Name</div><div class="plan-role">Graphic Designer</div>
    <p class="plan-copy">Lorem ipsum dolor sit amet, consectetur adipiscing elit, sed do eiusmod tempor incididunt ut labore et dolore magna aliqua. Ut enim ad minim veniam, quis nostrud exercitation.</p>
    <div class="plan-price">$10000</div>
    <a class="btn btn--solid" href="#">Read More</a>
  </div>
  <h2 class="section-title" style="top:359px">Our<br><span class="accent">Desigins</span><br>Package</h2>
</section>

<!-- CONTACT -->
<section class="section contact">
  <h2 class="section-title" style="top:50px">How<br><span class="accent">Find Us</span></h2>
  <div class="contact-item" style="top:222px">
    <svg width="30" height="30" viewBox="0 0 30 30" fill="none" stroke="#222" stroke-width="2" aria-hidden="true"><path d="M15 27s-9-9-9-15a9 9 0 0 1 18 0c0 6-9 15-9 15z"/><circle cx="15" cy="12" r="3"/></svg>
    <div><h4>Address</h4><p>Lorem ipsum dolor sit amet, consectetur adipiscing elit, sed do eiusmod tempor</p></div>
  </div>
  <div class="contact-item" style="top:324px">
    <svg width="30" height="30" viewBox="0 0 30 30" fill="none" stroke="#222" stroke-width="2" aria-hidden="true"><path d="M7 3l5 6-3 3c2 4 5 7 9 9l3-3 6 5-3 4C13 26 4 17 3 6z"/></svg>
    <div><h4>Call Us</h4><p>+100 555 0142<br>+100 555 0187</p></div>
  </div>
  <div class="contact-item" style="top:420px">
    <svg width="30" height="30" viewBox="0 0 30 30" fill="none" stroke="#222" stroke-width="2" aria-hidden="true"><rect x="3" y="7" width="24" height="16"/><path d="M3 7l12 9 12-9"/></svg>
    <div><h4>Email</h4><p>hello@novadesigns.example</p></div>
  </div>
  <div class="contact-item" style="top:500px">
    <svg width="30" height="30" viewBox="0 0 30 30" fill="none" stroke="#222" stroke-width="2" aria-hidden="true"><rect x="3" y="5" width="24" height="16"/><path d="M10 26h10M15 21v5"/></svg>
    <div><h4>Website</h4><p>www.novadesigns.example</p></div>
  </div>
  <div class="social-row" aria-label="Social links"><span></span><span></span><span></span><span></span><span></span></div>
  <div class="photo" role="img" aria-label="Desk with laptop and white modern chair" style="left:512px;top:0;width:688px;height:590px;background:linear-gradient(160deg,#4a3a30,#2a221d 55%,#8f8a84)"></div>
</section>

<!-- MAP -->
<section class="section map">
  <div class="photo" role="img" aria-label="Street map showing the studio location" style="inset:0;background:linear-gradient(180deg,#eceae5,#e3e1dc)"></div>
</section>

<footer class="section site-footer">Copyright © 2018, Nova Designs</footer>

</body>
</html>
```